Postcard Design

We offer facilitated group glasses in senior living facilities centered around memoir and life story writing. The postcards will go to administrators, activity directors and program directors at facilities, and potentially to librarians, staff and senior centers etc... So we want to say a little bit about WHY life writing is important to this population. I will upload a flyer I made myself. This will give you a sense of what we do and what we are trying to impart.
I've been using bright colors because they appeal to our population - blue is critical (Copper Wren Story Circle) and I'm down with anything else.
I have several images from google images that I've been using, but I'm not particularly attached to them. I did buy the rights to the blue owl guy and I have it in several formats and sizes.

I'm also including a power point that describes our course work, though I don't expect you to read it! Just trying to include anything that might be helpful. Any suggestions are most welcome!!! Thanks!

Industry/Entity Type

Group

```html
<!DOCTYPE html>
<html lang="en">
<head>
<meta charset="utf-8">
<title>Life Story Writing for Seniors – Postcard, front and back</title>
<link href="https://fonts.googleapis.com/css2?family=Sniglet&family=Gochi+Hand&family=Arimo:wght@400;700&family=Delius&display=swap" rel="stylesheet">
<style>
  :root {
    --bg: #e9e9ea;
    --paper: #f6f5f1;
    --card-white: #ffffff;
    --sky: #1ba3de;
    --title-blue: #2eaae6;
    --deep-blue: #2e6dba;
    --pale-blue: #9fd6f5;
    --sun: #f7e96b;
    --ink: #1b2a55;
    --note: #fbfbf8;
    --white: #ffffff;
    --black: #111111;
  }
  * { box-sizing: border-box; margin: 0; padding: 0; }
  html, body { width: 1200px; height: 800px; overflow: hidden; background: var(--bg); }

  .postcard {
    position: absolute;
    width: 1120px; height: 620px;
    background: var(--paper);
    overflow: hidden;
    box-shadow: 0 6px 18px rgba(0,0,0,.18);
    transform: scale(.6);
    transform-origin: 0 0;
  }
  .postcard--front { left: 264px; top: 14px; }
  .postcard--back  { left: 264px; top: 406px; background: var(--card-white); }
  .bands { position: absolute; inset: 0; }

  /* ---------- front ---------- */
  .mascot {
    position: absolute; left: 60px; top: 30px;
    width: 300px; height: 190px;
    border-radius: 14px;
    background: radial-gradient(ellipse at 45% 40%, #4fb9ea 0%, #7cc8ec 45%, #e9efe9 100%);
  }
  .title {
    position: absolute; left: 370px; top: 40px;
    font-family: "Sniglet", sans-serif; font-weight: 400; font-size: 36px;
    color: var(--title-blue); white-space: nowrap;
  }
  .subtitle {
    position: absolute; left: 440px; top: 92px;
    font-family: "Sniglet", sans-serif; font-size: 21px;
    color: var(--black); white-space: nowrap;
  }
  .photo {
    position: absolute; width: 178px; height: 146px;
    background: var(--white); padding: 6px;
    box-shadow: 0 2px 6px rgba(0,0,0,.25);
  }
  .photo span { display: block; width: 100%; height: 100%; }
  .photo--one { left: 482px; top: 150px; transform: rotate(2deg); }
  .photo--one span { background: linear-gradient(135deg, #d9d2c8, #b9c6d4 60%, #e7e1da); }
  .photo--two { left: 672px; top: 140px; transform: rotate(-1deg); }
  .photo--two span { background: linear-gradient(135deg, #cfd9e6, #a9b9cc 55%, #e4dccf); }
  .photo--three { left: 862px; top: 148px; transform: rotate(3deg); }
  .photo--three span { background: linear-gradient(135deg, #e4ddd0, #bcc7cf 55%, #d8cbb9); }

  .note {
    position: absolute; left: 70px; top: 225px;
    width: 440px; height: 270px;
    background: var(--note);
    transform: rotate(-7deg);
    box-shadow: 0 3px 8px rgba(0,0,0,.2);
    padding: 26px 26px 16px 40px;
    font-family: "Gochi Hand", cursive; font-size: 21px; line-height: 1.3;
    color: var(--ink);
  }
  .note__author { display: block; text-align: right; margin-top: 2px; }

  .why {
    position: absolute; left: 561px; top: 318px; width: 500px;
    font-family: "Arimo", sans-serif; font-size: 17px; line-height: 1.22;
    color: var(--white);
  }
  .brand {
    position: absolute; right: 40px; top: 512px;
    font-family: "Delius", sans-serif; font-size: 30px; white-space: nowrap;
    text-transform: uppercase;
  }
  .brand__name { color: var(--pale-blue); }
  .brand__person { color: var(--sun); }

  .contacts {
    position: absolute; right: 40px; top: 562px;
    display: flex; gap: 34px;
    font-family: "Delius", sans-serif; font-size: 26px; color: var(--white);
  }
  .contacts li { list-style: none; display: flex; align-items: center; gap: 10px; white-space: nowrap; }
  .contacts svg { width: 28px; height: 28px; }

  /* ---------- back ---------- */
  .back-title {
    position: absolute; left: 40px; top: 34px;
    font-family: "Sniglet", sans-serif; font-weight: 400; font-size: 38px;
    color: var(--title-blue); white-space: nowrap;
  }
  .back-subtitle {
    position: absolute; left: 40px; top: 86px;
    font-family: "Sniglet", sans-serif; font-size: 21px; color: var(--black);
  }
  .intro {
    position: absolute; left: 40px; top: 128px; width: 660px;
    font-family: "Arimo", sans-serif; font-size: 19px; line-height: 1.25;
    color: var(--black);
  }
  .about {
    position: absolute; left: 40px; top: 322px; width: 660px;
    color: var(--white); font-family: "Arimo", sans-serif;
  }
  .about h2 { font-size: 24px; font-weight: 700; margin-bottom: 8px; }
  .about p { font-size: 19px; line-height: 1.25; }

  .back-contact {
    position: absolute; left: 40px; top: 500px; width: 680px;
    font-family: "Delius", sans-serif; color: var(--white);
  }
  .back-contact__lead { font-size: 24px; }
  .back-contact .brand { position: static; font-size: 24px; margin-top: 4px; }
  .back-contact .contacts {
    position: static; margin-top: 6px; gap: 22px; font-size: 20px;
  }
  .back-contact .contacts svg { width: 22px; height: 22px; }
</style>
</head>
<body>
  <!-- Front -->
  <article class="postcard postcard--front">
    <svg class="bands" width="1120" height="620" viewBox="0 0 1120 620" aria-hidden="true">
      <path fill="var(--sky)" d="M0 250 L60 252 L120 246 L200 250 L300 254 L420 258 L470 256 L520 252 L540 260 L600 255 L660 258 L720 252 L780 258 L840 253 L900 257 L960 251 L1010 256 L1060 250 L1120 254 L1120 620 L0 620 Z"/>
      <path fill="var(--deep-blue)" d="M0 478 L80 482 L160 476 L240 484 L320 478 L400 486 L480 480 L560 490 L640 484 L720 490 L800 482 L880 489 L960 483 L1040 488 L1120 482 L1120 620 L0 620 Z"/>
    </svg>

    <div class="mascot" role="img" aria-label="Illustration of a blue owl perched on a flowering branch"></div>

    <h1 class="title">Life Story Writing For Seniors</h1>
    <p class="subtitle">8 Sessions with Follow-on Facilitation</p>

    <div class="photo photo--one" role="img" aria-label="Photo of a smiling senior woman in a group"><span></span></div>
    <div class="photo photo--two" role="img" aria-label="Photo of seniors gathered at a computer"><span></span></div>
    <div class="photo photo--three" role="img" aria-label="Photo of a group of seniors working together at a laptop"><span></span></div>

    <blockquote class="note">
      “This was my favorite experience of the last several years. I learned about myself and had such fun remembering the good times in my life. My children are thrilled with my writing! Ada was so kind and patient and helpful. This was really a wonderful class!”
      <span class="note__author">Marian, 79</span>
    </blockquote>

    <p class="why">The markers of a life well lived are the stories told, retold, and re-experienced. Life story writing captures the priceless and the poignant, the truly memorable and the quirkily remembered, the historic and the unique. It leaves a legacy of living history for future generations and brings enjoyment, satisfaction and closure to the author.</p>

    <p class="brand"><span class="brand__name">Copper Wren Story Circle</span> <span class="brand__person">Ada Lindqvist</span></p>

    <ul class="contacts">
      <li>
        <svg viewBox="0 0 28 28" aria-hidden="true"><rect x="2" y="2" width="24" height="24" rx="4" fill="var(--white)"/><path d="M11 7 h4 v4 h-3 v6 h3 v4 h-4 q-3 0 -3 -3 v-8 q0 -3 3 -3z" fill="var(--deep-blue)"/></svg>
        555-014-7390
      </li>
      <li>
        <svg viewBox="0 0 28 28" aria-hidden="true"><rect x="2" y="6" width="24" height="16" fill="none" stroke="var(--white)" stroke-width="2"/><path d="M2 6 L14 16 L26 6 M2 22 L11 13 M26 22 L17 13" fill="none" stroke="var(--white)" stroke-width="2"/></svg>
        ada@copperwren.biz
      </li>
      <li>
        <svg viewBox="0 0 28 28" aria-hidden="true"><g fill="none" stroke="var(--white)" stroke-width="2"><circle cx="14" cy="14" r="11"/><ellipse cx="14" cy="14" rx="5" ry="11"/><path d="M3 14 H25 M5 8 H23 M5 20 H23"/></g></svg>
        www.copperwren.biz
      </li>
    </ul>
  </article>

  <!-- Back -->
  <article class="postcard postcard--back">
    <svg class="bands" width="1120" height="620" viewBox="0 0 1120 620" aria-hidden="true">
      <path fill="var(--sky)" d="M0 300 L60 304 L130 298 L210 305 L300 299 L390 306 L480 300 L570 305 L660 299 L740 303 L740 620 L0 620 Z"/>
      <path fill="var(--deep-blue)" d="M0 486 L70 482 L150 490 L240 483 L330 491 L420 484 L510 490 L600 483 L680 489 L740 484 L740 620 L0 620 Z"/>
    </svg>

    <h1 class="back-title">Life Story Writing For Seniors</h1>
    <p class="back-subtitle">8 Sessions with Follow-on Facilitation</p>

    <p class="intro">Life writing classes are a gentle, joyful activity and help residents reconnect. Our facilitated groups guide seniors through recalling, writing and sharing cherished memories. Seniors learn that their stories span an entire century of change and how their lives intersected with history.</p>

    <section class="about">
      <h2>ABOUT</h2>
      <p>Ada Lindqvist has years of experience working with older adults, including memory care programs and the Parkside Wellness Center, where she led weekly writing circles. She has personalized activities for every ability and brings warmth to each session.</p>
    </section>

    <div class="back-contact">
      <p class="back-contact__lead">For More Information Please Contact:</p>
      <p class="brand"><span class="brand__name">Copper Wren Story Circle</span> <span class="brand__person">Ada Lindqvist</span></p>
      <ul class="contacts">
        <li>
          <svg viewBox="0 0 28 28" aria-hidden="true"><rect x="2" y="2" width="24" height="24" rx="4" fill="var(--white)"/><path d="M11 7 h4 v4 h-3 v6 h3 v4 h-4 q-3 0 -3 -3 v-8 q0 -3 3 -3z" fill="var(--deep-blue)"/></svg>
          555-014-7390
        </li>
        <li>
          <svg viewBox="0 0 28 28" aria-hidden="true"><rect x="2" y="6" width="24" height="16" fill="none" stroke="var(--white)" stroke-width="2"/><path d="M2 6 L14 16 L26 6 M2 22 L11 13 M26 22 L17 13" fill="none" stroke="var(--white)" stroke-width="2"/></svg>
          ada@copperwren.biz
        </li>
        <li>
          <svg viewBox="0 0 28 28" aria-hidden="true"><g fill="none" stroke="var(--white)" stroke-width="2"><circle cx="14" cy="14" r="11"/><ellipse cx="14" cy="14" rx="5" ry="11"/><path d="M3 14 H25 M5 8 H23 M5 20 H23"/></g></svg>
          www.copperwren.biz
        </li>
      </ul>
    </div>
  </article>
</body>
</html>
```